BrackenQuayCards
Business Cards
BrackenQuayCards - Law
Creative Brief
Professional
Matthias Lowe
Publisher
4751 Henley Court, Juniper Business Pavilion, 2nd Floor, Carlsbad, California, 92417-3051
lowe@brackenquay.example
www.brackenquay.example
Need delivery as AI file. Must be able to edit to add names, contact info, etc.

```html
<!DOCTYPE html>
<html lang="en">
<head>
<meta charset="utf-8">
<title>BrackenQuayCards – Business Card</title>
<link href="https://fonts.googleapis.com/css2?family=Open+Sans:wght@400;600;700;800&display=swap" rel="stylesheet">
<style>
  :root{
    --bg:#e9eaec;
    --card:#ffffff;
    --ink:#1c1c1c;
    --muted:#5b5b5b;
    --soft:#b9b9b9;
    --gold:#c9a132;
    --gold-light:#e6c866;
    --black:#151515;
  }
  *{margin:0;padding:0;box-sizing:border-box}
  html,body{width:1200px;height:1006px;overflow:hidden}
  body{background:var(--bg);font-family:"Open Sans",Arial,sans-serif;color:var(--ink);position:relative}
  .card{position:absolute;left:220px;width:760px;height:434px;background:var(--card);border-radius:22px;overflow:hidden;box-shadow:0 6px 18px rgba(0,0,0,.12)}
  .card--front{top:50px}
  .card--back{top:522px}

  .front-bands{position:absolute;inset:0}
  .brand{position:absolute;left:48px;top:44px;display:flex;align-items:center;gap:14px}
  .brand__dot{width:22px;height:22px;border-radius:50%;background:var(--black)}
  .brand__name{font-weight:800;font-size:34px;letter-spacing:-.5px;color:var(--ink)}
  .brand__tagline{position:absolute;left:84px;top:92px;font-size:11px;font-weight:600;color:var(--muted);letter-spacing:.2px}

  .contact{position:absolute;left:48px;top:128px;list-style:none;font-size:12px;line-height:19px;color:var(--muted)}
  .contact li{display:flex;align-items:center;gap:10px}
  .contact svg{width:12px;height:12px;flex:none;fill:var(--muted)}

  .person{position:absolute;right:46px;top:290px;text-align:right}
  .person__name{font-size:20px;font-weight:600;color:var(--ink)}
  .person__role{font-size:14px;color:var(--muted);margin-top:2px}

  .web{position:absolute;left:130px;bottom:26px;font-size:15px;letter-spacing:2.5px;color:#fff;font-weight:600}

  .back-brand{position:absolute;left:0;right:0;top:150px;display:flex;justify-content:center;align-items:center;gap:14px}
  .back-brand__name{font-size:40px;font-weight:800;color:var(--soft);letter-spacing:-.5px}
  .back-brand__dot{width:22px;height:22px;border-radius:50%;background:var(--soft)}
  .back-web{position:absolute;left:0;right:0;top:232px;text-align:center;font-size:14px;letter-spacing:4px;color:var(--muted)}
</style>
</head>
<body>

<section class="card card--front">
  <svg class="front-bands" viewBox="0 0 760 434" preserveAspectRatio="none" aria-hidden="true">
    <defs>
      <linearGradient id="goldFill" x1="0" y1="0" x2="1" y2="0">
        <stop offset="0" stop-color="var(--gold)"/>
        <stop offset=".6" stop-color="var(--gold-light)"/>
        <stop offset="1" stop-color="var(--gold)"/>
      </linearGradient>
    </defs>
    <path d="M0 236 L180 236 Q210 236 230 262 L0 262 Z" fill="var(--black)"/>
    <path d="M0 270 L236 270 Q262 300 300 330 Q330 350 380 352 L440 352 Q480 352 500 380 L540 434 L0 434 Z" fill="url(#goldFill)"/>
    <path d="M0 434 L760 434 L760 430 L0 430 Z" fill="var(--gold)"/>
  </svg>

  <div class="brand">
    <span class="brand__dot"></span>
    <span class="brand__name">BrackenQuay Investor</span>
  </div>
  <p class="brand__tagline">Banking, Tax &amp; Legal Services for the Global Investor</p>

  <ul class="contact">
    <li><svg viewBox="0 0 12 12"><path d="M6 0a4 4 0 0 0-4 4c0 3 4 8 4 8s4-5 4-8a4 4 0 0 0-4-4zm0 5.5A1.5 1.5 0 1 1 6 2.5a1.5 1.5 0 0 1 0 3z"/></svg>4751 Henley Court, Juniper Business Pavilion, 2nd Floor,</li>
    <li><svg viewBox="0 0 12 12"></svg>Carlsbad, California, 92417-3051</li>
    <li><svg viewBox="0 0 12 12"><path d="M2.5 0l2 3-1.2 1.3a7 7 0 0 0 4.4 4.4L9 7.5l3 2-1.3 2.2C5.5 12 0 6.5.3 1.3z"/></svg>T: 555-014-2290</li>
    <li><svg viewBox="0 0 12 12"><rect x="1" y="3" width="10" height="7" rx="1"/></svg>F: 555-014-2291</li>
    <li><svg viewBox="0 0 12 12"><path d="M0 2h12v8H0zm1 1 5 4 5-4z"/></svg>lowe@brackenquay.example</li>
  </ul>

  <div class="person">
    <p class="person__name">Matthias Lowe</p>
    <p class="person__role">Publisher</p>
  </div>

  <p class="web">www.brackenquay.example</p>
</section>

<section class="card card--back">
  <div class="back-brand">
    <span class="back-brand__name">BrackenQuay</span>
    <span class="back-brand__dot"></span>
  </div>
  <p class="back-web">www.brackenquay.example</p>
</section>

</body>
</html>
```